Catering Menu

We are looking at revamping our catering menu to appeal to the corporate and home catering Market.
Attached is our current menu. These items are current, and are required on the new design.
Pictures to be added of platters of what we offer
we are a upmarket venue in Melbourne Australia
we are looking to offer an off site catering option for our clients.
we are aiming to appeal to home celebrations, office and corporate functions.
The menu must pop, and catch the eye of the customer.
this will be done in a mail drop also.
6 sided DL flyer.

Target Market(s)

General Catering for businesses & people at home

Industry/Entity Type

Restaurant

Requirements
Must have
• Pictures of catering food, clear lay out of menu and pricing

```html
<!DOCTYPE html>
<html lang="en">
<head>
<meta charset="utf-8">
<title>Ironbark Catering Menu</title>
<link href="https://fonts.googleapis.com/css2?family=Oswald:wght@500;700&family=Open+Sans:wght@400;600;700&display=swap" rel="stylesheet">
<style>
:root{
  --wood-dark:#3b2517;
  --wood-mid:#6a4429;
  --wood-light:#8a5c39;
  --cream:#f4ecdc;
  --cream-line:#dccfb4;
  --orange:#e2761f;
  --price:#c0392b;
  --ink:#3a2a1e;
  --muted:#7a6650;
  --white:#ffffff;
  --page:#ffffff;
}
*{box-sizing:border-box;margin:0;padding:0}
html,body{width:781px;height:1200px;overflow:hidden;background:var(--page)}
body{position:relative;font-family:"Open Sans",Arial,sans-serif;color:var(--ink)}
.sheet{position:absolute;left:0;width:781px;background:linear-gradient(100deg,var(--wood-dark) 0%,var(--wood-mid) 30%,var(--wood-light) 55%,var(--wood-mid) 78%,var(--wood-dark) 100%)}
.sheet.outer{top:0;height:520px}
.sheet.inner{top:565px;height:600px}
.fold{position:absolute;top:0;bottom:0;width:1px;background:rgba(0,0,0,.35)}
.sheet-label{position:absolute;left:0;width:781px;text-align:center;font-family:"Oswald",sans-serif;font-weight:500;font-size:12px;letter-spacing:2px;color:#444}
.menu-box{position:absolute;background:var(--cream);border-radius:3px;box-shadow:0 2px 5px rgba(0,0,0,.45);overflow:hidden}
.menu-box h2{background:var(--orange);color:var(--white);font-family:"Oswald",sans-serif;font-weight:500;font-size:13px;padding:4px 10px;letter-spacing:.5px}
.menu-body{padding:6px 10px}
.item{display:flex;justify-content:space-between;align-items:flex-start;border-bottom:1px dotted var(--cream-line);padding:3px 0}
.item-name{font-size:7.4px;font-weight:700;line-height:1.3}
.item-desc{font-size:6.4px;color:var(--muted);line-height:1.3;font-weight:400}
.price{font-size:7.6px;font-weight:700;color:var(--price);white-space:nowrap;padding-left:6px}
.note{font-size:6.4px;color:var(--muted);padding-top:4px}
.photo{position:absolute;border-radius:2px}
.venue-address{position:absolute;left:300px;top:160px;width:190px;text-align:center;color:var(--white);font-size:8px;line-height:1.5}
.venue-address strong{font-size:9px}
.brand{position:absolute;left:548px;top:30px;width:222px;display:flex;align-items:center;justify-content:flex-end;gap:7px}
.brand-mark{width:9px;height:9px;border-radius:50%;background:var(--white)}
.brand-name{font-family:"Open Sans",sans-serif;font-weight:600;font-size:20px;color:var(--white)}
.cover-title{position:absolute;left:540px;top:218px;width:230px;text-align:right;font-family:"Oswald",sans-serif;font-weight:700;color:var(--orange);font-size:34px;line-height:1.05}
.cover-sub{position:absolute;left:540px;top:298px;width:230px;text-align:right;font-family:"Oswald",sans-serif;font-weight:500;color:var(--white);font-size:15px;line-height:1.15}
.order{position:absolute;left:540px;top:348px;width:230px;text-align:right;color:var(--white);font-size:8.5px;line-height:1.5}
.order b{color:var(--orange)}
.fineprint{position:absolute;left:540px;top:402px;width:230px;text-align:right;color:#e9dcc6;font-size:6px}
</style>
</head>
<body>

<section class="sheet outer" aria-label="Outer page">
  <div class="fold" style="left:260px"></div>
  <div class="fold" style="left:520px"></div>

  <article class="menu-box" style="left:10px;top:8px;width:240px;height:240px">
    <h2>Breakfast</h2>
    <div class="menu-body">
      <div class="item"><div><div class="item-name">Bakery Fresh Croissants</div><div class="item-desc">With your choice of fillings</div></div><span class="price">$49.00</span></div>
      <div class="item"><div><div class="item-name">Ham &amp; Cheese</div><div class="item-desc">Leg ham, swiss cheese, tomato</div></div><span class="price">$55.00</span></div>
      <div class="item"><div><div class="item-name">Hot English Muffins</div><div class="item-desc">With your choice of fillings</div></div><span class="price">$52.00</span></div>
      <div class="item"><div><div class="item-name">Bacon &amp; Egg</div><div class="item-desc">Crispy bacon, free range egg, relish</div></div><span class="price">$58.00</span></div>
      <div class="item"><div><div class="item-name">Pancakes</div><div class="item-desc">With your choice of toppings</div></div><span class="price">$45.00</span></div>
      <div class="item"><div><div class="item-name">Fresh Fruit Platter</div><div class="item-desc">Seasonal fruit, yoghurt and honey</div></div><span class="price">$60.00</span></div>
      <p class="note">Served with juice and yogurt</p>
    </div>
  </article>

  <article class="menu-box" style="left:10px;top:256px;width:240px;height:256px">
    <h2>Morning &amp; Afternoon Tea Platters</h2>
    <div class="menu-body">
      <div class="item"><div><div class="item-name">Assorted Cake Platter</div><div class="item-desc">Slices, tarts and mini muffins</div></div><span class="price">$65.00</span></div>
      <div class="item"><div><div class="item-name">An assortment of homemade</div><div class="item-desc">Cookies, brownies and friands baked daily</div></div><span class="price">$55.00</span></div>
      <div class="item"><div><div class="item-name">Scones with jam and cream</div><div class="item-desc">Warm scones, berry jam, whipped cream</div></div><span class="price">$48.00</span></div>
      <div class="item"><div><div class="item-name">Savoury Mini Pastries</div><div class="item-desc">Sausage rolls, quiches and party pies</div></div><span class="price">$62.00</span></div>
      <div class="item"><div><div class="item-name">Cheese &amp; Cracker Board</div><div class="item-desc">Local cheeses, dried fruit and nuts</div></div><span class="price">$75.00</span></div>
      <div class="item"><div><div class="item-name">Gourmet Finger Sandwiches</div><div class="item-desc">Selection of classic fillings</div></div><span class="price">$58.00</span></div>
      <p class="note">Served with tea and coffee</p>
    </div>
  </article>

  <div class="venue-address">
    <strong>Ironbark Square Centre</strong><br>
    P + 03 9000 1234<br>
    18 Market Road, Sunbury VIC 3429
  </div>

  <div class="brand"><span class="brand-mark"></span><span class="brand-name">Ironbark</span></div>
  <div class="photo" role="img" aria-label="Photo of a plated gourmet catering dish" style="left:548px;top:76px;width:222px;height:138px;background:linear-gradient(135deg,#7a3a1e,#c7652e 45%,#e0a24a 70%,#4f6b2a)"></div>
  <h1 class="cover-title">Catering<br>Menu</h1>
  <p class="cover-sub">Your guide to our platter options available</p>
  <p class="order"><b>To order please:</b><br>Call 03 9000 1234<br><b>Email</b> events@ironbarkcatering.com.au</p>
  <p class="fineprint">A minimum 24 hours notice is required</p>
</section>
<div class="sheet-label" style="top:540px">OUTER PAGE</div>

<section class="sheet inner" aria-label="Inner page">
  <div class="fold" style="left:260px"></div>
  <div class="fold" style="left:520px"></div>

  <article class="menu-box" style="left:10px;top:10px;width:240px;height:342px">
    <h2>Hot Lunch Platters</h2>
    <div class="menu-body">
      <div class="item"><div><div class="item-name">Selection of vegetable dishes</div><div class="item-desc">Roasted seasonal vegetables with herbs</div></div><span class="price">$65.00</span></div>
      <div class="item"><div><div class="item-name">Two choices of meats</div><div class="item-desc">Carved roast beef and herb chicken</div></div><span class="price">$89.00</span></div>
      <div class="item"><div><div class="item-name">Chicken and vegetable curry</div><div class="item-desc">Served with steamed rice and naan</div></div><span class="price">$79.00</span></div>
      <div class="item"><div><div class="item-name">Beef lasagne</div><div class="item-desc">Slow cooked ragu, bechamel, parmesan</div></div><span class="price">$72.00</span></div>
      <div class="item"><div><div class="item-name">Your selection of meats</div><div class="item-desc">Lamb, pork or chicken with gravy</div></div><span class="price">$95.00</span></div>
      <div class="item"><div><div class="item-name">Pasta bake</div><div class="item-desc">Penne, tomato, basil and mozzarella</div></div><span class="price">$62.00</span></div>
      <div class="item"><div><div class="item-name">Hot finger food</div><div class="item-desc">Spring rolls, dim sims and arancini</div></div><span class="price">$68.00</span></div>
      <div class="item"><div><div class="item-name">Crispy potato wedges</div><div class="item-desc">With sour cream and sweet chilli</div></div><span class="price">$35.00</span></div>
      <p class="note">Served with bread rolls and butter</p>
    </div>
  </article>

  <article class="menu-box" style="left:10px;top:362px;width:240px;height:228px">
    <h2>Cold Lunch Platters</h2>
    <div class="menu-body">
      <div class="item"><div><div class="item-name">Antipasto Platter</div><div class="item-desc">Cured meats, olives, grilled vegetables</div></div><span class="price">$85.00</span></div>
      <div class="item"><div><div class="item-name">Seafood Platter</div><div class="item-desc">Prawns, smoked salmon and oysters</div></div><span class="price">$120.00</span></div>
      <div class="item"><div><div class="item-name">Cold Meat Platter</div><div class="item-desc">Ham, turkey, roast beef and pickles</div></div><span class="price">$78.00</span></div>
      <div class="item"><div><div class="item-name">Sushi Platter</div><div class="item-desc">Assorted rolls with soy and wasabi</div></div><span class="price">$70.00</span></div>
    </div>
  </article>

  <article class="menu-box" style="left:270px;top:10px;width:240px;height:300px">
    <h2>Sandwiches/Wraps/Focaccia Platters</h2>
    <div class="menu-body">
      <div class="item"><div><div class="item-name">Sandwich Platter</div></div><span class="price">$55.00</span></div>
      <div class="item"><div><div class="item-name">Wrap Platter</div></div><span class="price">$60.00</span></div>
      <div class="item"><div><div class="item-name">Focaccia Platter</div></div><span class="price">$65.00</span></div>
      <div class="item"><div><div class="item-name">With your choice of 5 fillings listed below</div><div class="item-desc">Ham, cheese and tomato<br>Chicken, avocado and mayonnaise<br>Roast beef, mustard and rocket<br>Egg, lettuce and chives<br>Tuna, corn and mayonnaise<br>Turkey, brie and cranberry<br>Salami, provolone and capsicum<br>Grilled vegetables and hummus<br>Smoked salmon and cream cheese<br>Bacon, lettuce and tomato</div></div></div>
    </div>
  </article>
  <div class="photo" role="img" aria-label="Photo of a stacked club sandwich" style="left:270px;top:318px;width:240px;height:272px;background:linear-gradient(160deg,#d9a75a,#b8742f 40%,#6f9a3a 60%,#c33f2a 75%,#e6c48a)"></div>

  <article class="menu-box" style="left:530px;top:10px;width:240px;height:296px">
    <h2>Drink Platters</h2>
    <div class="menu-body">
      <div class="item"><div><div class="item-name">Soft drinks</div><div class="item-desc">Assorted 375ml cans</div></div><span class="price">$3.50</span></div>
      <div class="item"><div><div class="item-name">Bottled water</div><div class="item-desc">Still and sparkling</div></div><span class="price">$3.00</span></div>
      <div class="item"><div><div class="item-name">Orange juice</div><div class="item-desc">Freshly squeezed, per litre</div></div><span class="price">$12.00</span></div>
      <div class="item"><div><div class="item-name">Tea and coffee</div><div class="item-desc">Per person, with milk and sugar</div></div><span class="price">$4.50</span></div>
      <div class="item"><div><div class="item-name">Wine selection</div><div class="item-desc">Local red, white and sparkling</div></div><span class="price">$28.00</span></div>
      <div class="item"><div><div class="item-name">Beer selection</div><div class="item-desc">Local craft beers, per dozen</div></div><span class="price">$60.00</span></div>
    </div>
  </article>

  <article class="menu-box" style="left:530px;top:316px;width:240px;height:274px">
    <h2>Salads</h2>
    <div class="menu-body">
      <div class="item"><div><div class="item-name">Garden salad</div><div class="item-desc">Mixed leaves, tomato, cucumber</div></div><span class="price">$35.00</span></div>
      <div class="item"><div><div class="item-name">Caesar salad</div><div class="item-desc">Cos, bacon, croutons, parmesan</div></div><span class="price">$42.00</span></div>
      <div class="item"><div><div class="item-name">Greek salad</div><div class="item-desc">Feta, olives, red onion, oregano</div></div><span class="price">$40.00</span></div>
      <div class="item"><div><div class="item-name">Potato salad</div><div class="item-desc">Chives, egg and creamy dressing</div></div><span class="price">$36.00</span></div>
    </div>
    <div class="photo" role="img" aria-label="Photo of a fresh leafy salad bowl" style="left:10px;bottom:8px;width:220px;height:80px;background:linear-gradient(120deg,#5f8f2e,#9cc14a 45%,#d84a2e 70%,#f0e2b8)"></div>
  </article>
</section>
<div class="sheet-label" style="top:1175px">INNER PAGE</div>

</body>
</html>
```